Veltharon Partner Needed Design for EKR Management Web App

We need a web app design for a new cloud based software called "Pruncely QMS". This software will be used by enterprises with EKR standards, and does manages audit (for both internal and external).
The application will be used to keep track of the tasks, activities and work process required to achieve the EKR process and audit completion.
It also provides a dashboard for different roles to access the required information and analysis at their fingertips. The standard screen currently available on the system has been provided in the attachment.
We need the design to be done based on a modern UI / UX, preferably flat UI based upon bootstrap.

Industry/Entity Type

Software

Coding

Coded - Design and coding required

Number of Pages Required

5+ page

Font styles to use
Sans Serif

Colors
f37122
ec1f27
9bcb3c

Requirements
Must have
• - Modern, Flat UI, based on Bootstrap.
• - Open for Suggestion on how to improve UX

```html
<!DOCTYPE html>
<html lang="en">
<head>
<meta charset="utf-8">
<title>Pruncely QMS – Standard Overview</title>
<link rel="stylesheet" href="https://fonts.googleapis.com/css2?family=Roboto:wght@300;400;500&display=swap">
<style>
:root{
  --orange:#f37122;
  --green:#9bcb3c;
  --red:#ec1f27;
  --title-red:#ee4a3f;
  --nav-bg:#f0f0f0;
  --nav-line:#d4d4d4;
  --card-bg:#f7f7f7;
  --tile-bg:#f2f2f2;
  --tile-edge:#bdbdbd;
  --text:#333;
  --muted:#666;
  --rule:#e0e0e0;
  --box-line:#e2e2e2;
}
*{box-sizing:border-box;margin:0;padding:0}
html,body{width:1200px;height:1071px;overflow:hidden;background:#fff}
body{position:relative;font-family:'Roboto',sans-serif;color:var(--text)}

.topbar{position:absolute;left:0;top:0;width:1200px;height:50px;background:var(--nav-bg);border-bottom:1px solid var(--nav-line)}
.brand{position:absolute;left:76px;top:14px;font-size:19px;font-weight:500;color:#333;letter-spacing:.3px}
.menu{position:absolute;top:19px;font-size:12.5px;color:#444;letter-spacing:.3px}
.menu .caret{display:inline-block;margin-left:8px;border-left:4px solid transparent;border-right:4px solid transparent;border-top:4px solid #999;vertical-align:middle}

.section-title{position:absolute;left:75px;font-size:28px;font-weight:300}
.section-title.overview{top:76px;color:var(--title-red)}
.section-title.pending{top:762px;color:#555}
.rule{position:absolute;left:75px;width:1050px;height:1px;background:var(--rule)}

.standard-card{position:absolute;top:138px;width:330px;height:594px;background:var(--card-bg);border-top:4px solid var(--orange)}
.standard-name{position:absolute;top:32px;width:100%;text-align:center;font-size:21px;font-weight:300;color:#333;letter-spacing:.5px}
.coverage{position:absolute;left:76px;top:72px;width:178px;height:178px}
.coverage-value{position:absolute;left:0;top:143px;width:100%;text-align:center;font-size:29px;font-weight:400;color:#333}
.coverage-label{position:absolute;top:270px;width:100%;text-align:center;font-size:14px;color:var(--muted)}

.countdown{position:absolute;left:24px;top:310px;width:282px;height:133px;background:#fff;border:2px solid var(--box-line);border-radius:3px;text-align:center}
.countdown svg{position:absolute;left:117px;top:12px}
.countdown-days{position:absolute;top:70px;width:100%;font-size:25px;font-weight:300;color:#333}
.countdown-note{position:absolute;top:104px;width:100%;font-size:14px;font-weight:300;color:var(--muted)}

.action-table{position:absolute;left:24px;top:457px;width:282px;height:116px;background:#fff;border:2px solid var(--box-line);border-radius:3px;border-collapse:separate;border-spacing:0}
.action-table th,.action-table td{text-align:left;padding-left:17px;height:38px}
.action-table th{font-size:12.5px;font-weight:400;color:#333;border-bottom:2px solid var(--box-line);height:35px}
.action-table td{font-size:12px;font-weight:300;color:#444}
.action-table tr.open td{border-bottom:2px solid var(--box-line)}

.task-tile{position:absolute;top:828px;width:182px;height:174px;background:var(--tile-bg);border-bottom:4px solid var(--tile-edge);text-align:center}
.task-count{position:absolute;top:22px;width:100%;font-size:74px;font-weight:400;color:#666;line-height:1}
.task-label{position:absolute;top:122px;width:100%;font-size:14.5px;color:#333;letter-spacing:.3px}
</style>
</head>
<body>

<header class="topbar">
  <div class="brand">Pruncely</div>
  <nav>
    <span class="menu" style="left:226px">Home</span>
    <span class="menu" style="left:292px">Quality Management<span class="caret"></span></span>
    <span class="menu" style="left:443px">Master Maintenance</span>
    <span class="menu" style="left:593px">About</span>
    <span class="menu" style="left:659px">Contact</span>
  </nav>
</header>

<h1 class="section-title overview">Standard Overview</h1>
<div class="rule" style="top:118px"></div>

<!-- Card 1 -->
<section class="standard-card" style="left:75px">
  <h2 class="standard-name">EKR 9001</h2>
  <svg class="coverage" viewBox="0 0 178 178">
    <circle cx="89" cy="89" r="89" fill="#fff"/>
    <path d="M89 0 A89 89 0 0 1 178 89 L152 89 A63 63 0 0 0 89 26 Z" fill="var(--orange)"/>
    <circle cx="89" cy="89" r="64" fill="#e6e6e6"/>
    <circle cx="89" cy="89" r="63" fill="#f4f4f4"/>
  </svg>
  <div class="coverage-value">30%</div>
  <div class="coverage-label">Audit Coverage</div>
  <div class="countdown">
    <svg width="46" height="48" viewBox="0 0 46 48" fill="none" stroke="var(--orange)" stroke-width="3.5" stroke-linecap="round">
      <circle cx="23" cy="26" r="17"/><path d="M23 16v10h8"/><path d="M10 42l-3 4M36 42l3 4"/>
      <path d="M3 12a8 8 0 0 1 11-9z" fill="var(--orange)"/><path d="M43 12a8 8 0 0 0-11-9z" fill="var(--orange)"/>
    </svg>
    <div class="countdown-days">32 Days</div>
    <div class="countdown-note">Till Next External Audit</div>
  </div>
  <table class="action-table">
    <tr><th>TYPE</th><th>CAR</th><th>PAR</th></tr>
    <tr class="open"><td>Open</td><td>12</td><td>3</td></tr>
    <tr><td>Closed</td><td>4</td><td>2</td></tr>
  </table>
</section>

<!-- Card 2 -->
<section class="standard-card" style="left:435px">
  <h2 class="standard-name">EKR 9001</h2>
  <svg class="coverage" viewBox="0 0 178 178">
    <circle cx="89" cy="89" r="89" fill="#fff"/>
    <path d="M89 0 A89 89 0 0 1 178 89 L152 89 A63 63 0 0 0 89 26 Z" fill="var(--green)"/>
    <circle cx="89" cy="89" r="64" fill="#e6e6e6"/>
    <circle cx="89" cy="89" r="63" fill="#f4f4f4"/>
  </svg>
  <div class="coverage-value">30%</div>
  <div class="coverage-label">Audit Coverage</div>
  <div class="countdown">
    <svg width="46" height="48" viewBox="0 0 46 48" fill="none" stroke="var(--green)" stroke-width="3.5" stroke-linecap="round">
      <circle cx="23" cy="26" r="17"/><path d="M23 16v10h8"/><path d="M10 42l-3 4M36 42l3 4"/>
      <path d="M3 12a8 8 0 0 1 11-9z" fill="var(--green)"/><path d="M43 12a8 8 0 0 0-11-9z" fill="var(--green)"/>
    </svg>
    <div class="countdown-days">109 Days</div>
    <div class="countdown-note">Till Next External Audit</div>
  </div>
  <table class="action-table">
    <tr><th>TYPE</th><th>CAR</th><th>PAR</th></tr>
    <tr class="open"><td>Open</td><td>12</td><td>3</td></tr>
    <tr><td>Closed</td><td>4</td><td>2</td></tr>
  </table>
</section>

<!-- Card 3 -->
<section class="standard-card" style="left:795px">
  <h2 class="standard-name">EKR 9001</h2>
  <svg class="coverage" viewBox="0 0 178 178">
    <circle cx="89" cy="89" r="89" fill="#fff"/>
    <path d="M89 0 A89 89 0 0 1 178 89 L152 89 A63 63 0 0 0 89 26 Z" fill="var(--red)"/>
    <circle cx="89" cy="89" r="64" fill="#e6e6e6"/>
    <circle cx="89" cy="89" r="63" fill="#f4f4f4"/>
  </svg>
  <div class="coverage-value">30%</div>
  <div class="coverage-label">Audit Coverage</div>
  <div class="countdown">
    <svg width="46" height="48" viewBox="0 0 46 48" fill="none" stroke="var(--red)" stroke-width="3.5" stroke-linecap="round">
      <circle cx="23" cy="26" r="17"/><path d="M23 16v10h8"/><path d="M10 42l-3 4M36 42l3 4"/>
      <path d="M3 12a8 8 0 0 1 11-9z" fill="var(--red)"/><path d="M43 12a8 8 0 0 0-11-9z" fill="var(--red)"/>
    </svg>
    <div class="countdown-days">72 Days</div>
    <div class="countdown-note">Till Next External Audit</div>
  </div>
  <table class="action-table">
    <tr><th>TYPE</th><th>CAR</th><th>PAR</th></tr>
    <tr class="open"><td>Open</td><td>12</td><td>3</td></tr>
    <tr><td>Closed</td><td>4</td><td>2</td></tr>
  </table>
</section>

<h1 class="section-title pending">My Pending Task</h1>
<div class="rule" style="top:804px"></div>

<div class="task-tile" style="left:75px"><div class="task-count">0</div><div class="task-label">Audit Management</div></div>
<div class="task-tile" style="left:293px"><div class="task-count">3</div><div class="task-label">CAR</div></div>
<div class="task-tile" style="left:509px"><div class="task-count">2</div><div class="task-label">PAR</div></div>
<div class="task-tile" style="left:726px"><div class="task-count">8</div><div class="task-label">Document Control</div></div>
<div class="task-tile" style="left:943px"><div class="task-count">1</div><div class="task-label">Annual Review</div></div>

</body>
</html>
```